Need innovative card design for tech start up

We are a Santa Monica based marketing analytics software start up called Brightwell Metrics. We're launching a platform that will help advertisers better measure and optimize their marketing spend by using advanced algorithmic analytic. While our subject matter is complicated, we want to convey simple, clean, curated. We also want to stand out - ad tech is a sea of sameness and we need to have some individuality. We have an established color palette and would like to see a design we could print in each tone (teal, tangerine, grey), but it doesn't require the card to be monochromatic. The font used is DENSE.

Marketing

```html
<!DOCTYPE html>
<html lang="en">
<head>
<meta charset="utf-8">
<title>Brightwell Metrics – Business Card</title>
<link rel="stylesheet" href="https://fonts.googleapis.com/css2?family=Open+Sans:wght@400;600&display=swap">
<style>
  :root {
    --page-bg: #ececec;
    --card-white: #ffffff;
    --card-dark: #4a4a4a;
    --tangerine: #f7941d;
    --text-grey: #6d6d6d;
    --text-light: #f2f2f2;
    --panel-white: #ffffff;
  }
  * { box-sizing: border-box; margin: 0; padding: 0; }
  html, body {
    width: 1200px; height: 900px; overflow: hidden;
    background: var(--page-bg);
    font-family: "Open Sans", sans-serif;
  }
  .sheet {
    width: 1200px; height: 900px;
    display: flex; align-items: center; justify-content: center; gap: 44px;
  }
  .card {
    width: 520px; height: 298px;
    border-radius: 22px;
    overflow: hidden;
    position: relative;
    box-shadow: 0 10px 24px rgba(0,0,0,0.18);
  }

  /* Front */
  .card-front { background: var(--card-white); }
  .front-top { position: absolute; left: 0; top: 0; width: 100%; height: 160px; }
  .brand-lockup {
    position: absolute; left: 22px; top: 30px;
    display: flex; flex-direction: column; gap: 10px;
  }
  .brand-square { width: 92px; height: 92px; background: var(--tangerine); }
  .brand-name {
    font-size: 13px; font-weight: 600; letter-spacing: 0.02em;
    color: var(--tangerine); text-transform: uppercase; white-space: nowrap;
  }
  .person { position: absolute; right: 30px; top: 24px; text-align: right; }
  .person-name { font-size: 17px; font-weight: 600; color: var(--tangerine); }
  .person-title { font-size: 15px; color: var(--text-grey); margin-top: 2px; }
  .accent-rule {
    position: absolute; left: 0; top: 160px; width: 100%; height: 6px;
    background: var(--tangerine);
  }
  .front-bottom {
    position: absolute; left: 0; top: 166px; width: 100%; bottom: 0;
    background: var(--card-dark);
  }
  .contact-list {
    list-style: none; position: absolute; left: 24px; top: 14px;
    font-size: 12.5px; line-height: 16.5px; color: var(--text-light);
  }
  .contact-list li { display: flex; align-items: center; gap: 5px; white-space: nowrap; }
  .contact-list svg { width: 11px; height: 11px; flex: none; }
  .contact-list .indent { padding-left: 16px; }

  /* Back */
  .card-back {
    background: var(--card-dark);
    display: flex; align-items: center; justify-content: center;
  }
  .back-panel {
    width: 124px; height: 150px; background: var(--panel-white);
    display: flex; flex-direction: column; align-items: center; justify-content: center; gap: 10px;
  }
  .back-panel .brand-square { width: 100px; height: 92px; }
  .back-panel .brand-name { font-size: 10px; }
</style>
</head>
<body>
<main class="sheet">

  <section class="card card-front" aria-label="Card front">
    <div class="front-top">
      <div class="brand-lockup">
        <div class="brand-square"></div>
        <span class="brand-name">Brightwell Metrics</span>
      </div>
      <div class="person">
        <p class="person-name">Dana Whitlock</p>
        <p class="person-title">Founder/CEO</p>
      </div>
    </div>
    <div class="accent-rule"></div>
    <div class="front-bottom">
      <ul class="contact-list">
        <li><svg viewBox="0 0 12 12"><path fill="#f7941d" d="M2.5 1h2l1 3-1.3 1a6 6 0 0 0 2.8 2.8L8 6.5l3 1v2A1.5 1.5 0 0 1 9.5 11 8.5 8.5 0 0 1 1 2.5 1.5 1.5 0 0 1 2.5 1z"/></svg>707-555-0147 x12</li>
        <li><svg viewBox="0 0 12 12"><rect x="3" y="0.5" width="6" height="11" rx="1" fill="#f7941d"/><rect x="4" y="2" width="4" height="6.5" fill="#4a4a4a"/></svg>707-555-0182</li>
        <li><svg viewBox="0 0 12 12"><rect x="0.5" y="2.5" width="11" height="7" fill="#f7941d"/><path d="M0.5 2.5 6 7l5.5-4.5" stroke="#4a4a4a" fill="none"/></svg>dana@brightwellmetrics.com</li>
        <li><svg viewBox="0 0 12 12"><circle cx="6" cy="6" r="5" fill="none" stroke="#f7941d" stroke-width="1.3"/><ellipse cx="6" cy="6" rx="2" ry="5" fill="none" stroke="#f7941d"/><path d="M1 6h10" stroke="#f7941d"/></svg>www.brightwellmetrics.com</li>
        <li><svg viewBox="0 0 12 12"><path fill="#f7941d" d="M6 1 0.5 6H2v5h3V8h2v3h3V6h1.5z"/></svg>1840 Harbor View, suite 410</li>
        <li class="indent">Marlow Cove, CA 93050</li>
      </ul>
    </div>
  </section>

  <section class="card card-back" aria-label="Card back">
    <div class="back-panel">
      <div class="brand-square"></div>
      <span class="brand-name">Brightwell Metrics</span>
    </div>
  </section>

</main>
</body>
</html>
```